PowerPoint Presentation 10 Slides Needed with custom graphics and possibly animated gifs

I'm creating an educational webinar for professionals. I have 10 slides that need special treatment--effective visuals that really Deliverables10 PowerPoint slides in shared PPT fileWith 10 or more images that communicate the message described in the slides notes for each slide.DeadlineSlides will be used in a PowerPoint presentation Monday, Dec 10.Due date is Friday, Dec 7.Design GuidanceSee attached deck for existing design template/theme (with colors/logo)You should match the designAnimations should be delivered as GIF files that can appear in a slideAnimation can last 4 to 10 seconds.Instead of animations, photos from Glimmerbay can be recommended (I have an account and can provide the final file to use).

```html
<!DOCTYPE html>
<html lang="en">
<head>
<meta charset="utf-8">
<title>Lets Get Back To Basics – Slide Board</title>
<link rel="stylesheet" href="https://fonts.googleapis.com/css2?family=Bebas+Neue&family=Open+Sans:wght@400;600;700&display=swap">
<style>
  :root{
    --blue:#21409a;
    --blue-soft:#2d4ca6;
    --green:#1b7a3c;
    --grey-text:#555a5f;
    --slide-grey:#e3e4e5;
    --paper:#ffffff;
    --ink:#231f20;
    --cookie-light:#c98d4a;
    --cookie-dark:#7a4a22;
  }
  *{box-sizing:border-box;margin:0;padding:0}
  html,body{width:1200px;height:1056px;overflow:hidden;background:var(--paper)}
  .canvas{width:1200px;height:1056px;position:relative;overflow:hidden;background:var(--paper)}
  .board{position:absolute;left:0;top:0;width:1427px;height:1256px;transform:scale(.8409);transform-origin:0 0;border:1px solid #777;font-family:"Open Sans",sans-serif}
  .board-title{position:absolute;right:49px;top:54px;font-family:"Bebas Neue",sans-serif;font-size:30px;color:var(--ink);letter-spacing:.3px}
  .slide-no{position:absolute;font-family:"Open Sans",sans-serif;font-size:22px;color:var(--ink);transform:translate(-50%,-50%)}

  .slide{position:absolute;width:591px;height:331px;overflow:hidden;
    background:radial-gradient(ellipse 70% 80% at 88% 8%, #ffffff 0%, #f2f2f3 35%, var(--slide-grey) 75%)}
  .slide svg.layer{position:absolute;left:0;top:0;width:100%;height:100%}
  .abs{position:absolute}
  .center{transform:translate(-50%,-50%);text-align:center}
  .bar{position:absolute;left:0;width:17px;height:139px;background:var(--green)}
  .bar--blue{background:var(--blue)}
  .display{font-family:"Bebas Neue",sans-serif;font-weight:400}

  .mini-brand{position:absolute;top:24px;right:35px;display:flex;align-items:center;gap:9px}
  .mini-brand__deck{font-family:"Bebas Neue",sans-serif;font-size:9.5px;line-height:8px;color:var(--blue)}
  .mini-brand__mark{width:36px;height:36px;border-radius:50%;border:1.2px solid var(--green);background:#fff;
    display:flex;align-items:center;justify-content:center;font-size:7px;line-height:8px;color:var(--blue);text-align:center}

  /* slide 1 */
  .slide--cover{background:var(--blue)}
  .cover__art{position:absolute;left:145px;top:85px;width:415px;height:220px;border-radius:8px;
    background:radial-gradient(ellipse at 50% 50%, var(--blue-soft) 0%, var(--blue) 80%)}
  .cover__title{left:264px;top:189px;font-size:36px;color:#fff;white-space:nowrap}
  .cover__brand{position:absolute;left:472px;top:17px;width:92px;height:92px;border-radius:50%;background:#fff;
    display:flex;align-items:center;justify-content:center;text-align:center;font-size:14px;line-height:16px;color:var(--blue)}

  /* slide 4 */
  .cookie__head{left:50px;top:94px;font-size:64px;line-height:52px;color:var(--blue)}
  .cookie__lead{left:406px;font-size:13.5px;line-height:19px;color:var(--green);width:220px}
  .cookie__art{position:absolute;left:322px;top:148px;width:184px;height:116px;border-radius:6px;
    background:radial-gradient(ellipse at 45% 45%, var(--cookie-light) 0%, #b98a5c 55%, #e0d7cd 100%)}

  /* slide 2 */
  .share__term{left:31px;top:105px;color:var(--blue);font-size:18px;line-height:21px}
  .share__term b{font-weight:700}
  .share__body{left:33px;top:161px;width:125px;font-size:12px;line-height:16.8px;color:var(--grey-text)}
  .share__lead{left:342px;top:100px;font-size:10px;color:var(--green);white-space:nowrap}
  .share__role{font-size:29px;line-height:25px;color:#fff}
  .share__note{left:364px;top:285px;font-size:10px;color:var(--green);white-space:nowrap}

  /* slide 5 */
  .throw__title{left:292px;top:38px;font-size:18px;font-weight:700;color:var(--blue);white-space:nowrap}
  .throw__head{font-size:24px;line-height:26px;color:var(--green);white-space:nowrap}
  .throw__small{font-size:8px;line-height:12.5px;color:var(--grey-text);margin-top:4px;white-space:nowrap}
  .throw__face{font-size:15px;color:var(--ink);margin-top:4px}

  /* slide 3 */
  .flow__badge{font-size:15px;line-height:12px;color:#fff}
  .flow__caption{font-size:9px;color:var(--green);white-space:nowrap}

  /* slide 6 */
  .you__title{left:341px;top:41px;font-size:18px;font-weight:700;color:var(--blue)}
  .you__bubble{font-size:11px;line-height:13px;font-weight:700;color:var(--blue);white-space:nowrap}
</style>
</head>
<body>
<div class="canvas">
<div class="board">

  <div class="board-title">First 6 slides modified</div>
  <div class="slide-no" style="left:58px;top:340px">1</div>
  <div class="slide-no" style="left:58px;top:617px">2</div>
  <div class="slide-no" style="left:58px;top:893px">3</div>
  <div class="slide-no" style="left:1368px;top:340px">4</div>
  <div class="slide-no" style="left:1368px;top:617px">5</div>
  <div class="slide-no" style="left:1368px;top:893px">6</div>

  <!-- Slide 1: cover -->
  <section class="slide slide--cover" style="left:92px;top:141px">
    <div class="cover__art" role="img" aria-label="Illustration of scattered outline speech bubbles with one filled green bubble"></div>
    <div class="abs center display cover__title">Lets get back to basics</div>
    <div class="cover__brand">Cortland<br>Circle</div>
  </section>

  <!-- Slide 4: cookie question -->
  <section class="slide" style="left:729px;top:140px">
    <div class="bar" style="top:111px"></div>
    <div class="abs display cookie__head">Do you<br>like my<br>cookie?</div>
    <div class="abs center cookie__lead" style="top:116px">Imaging communication is<br>like sharing a cookie…</div>
    <div class="cookie__art" role="img" aria-label="Photo of two chocolate chip cookies cut into speech bubble shapes"></div>
    <div class="mini-brand"><div class="mini-brand__deck">Lets get<br>back to<br>basics</div><div class="mini-brand__mark">Cortland<br>Circle</div></div>
  </section>

  <!-- Slide 2: giver, gift, recipient -->
  <section class="slide" style="left:92px;top:492px">
    <div class="bar" style="top:106px;width:16px"></div>
    <div class="abs share__term"><b>Commicare</b><br>means to share</div>
    <div class="abs share__body">The word Communication comes from late Middle English: from Old French from the verb communicare ‘to share’</div>
    <div class="abs center share__lead">To share, there must be at least:</div>
    <svg class="layer" viewBox="0 0 591 331">
      <g fill="var(--blue)" stroke="var(--green)" stroke-width="1">
        <circle cx="231" cy="192" r="57" fill="#fff"/><circle cx="231" cy="192" r="51" stroke="none"/>
        <circle cx="363" cy="192" r="57" fill="#fff"/><circle cx="363" cy="192" r="51" stroke="none"/>
        <circle cx="499" cy="192" r="57" fill="#fff"/><circle cx="499" cy="192" r="51" stroke="none"/>
      </g>
    </svg>
    <div class="abs center display share__role" style="left:231px;top:193px">Giver</div>
    <div class="abs center display share__role" style="left:363px;top:193px">The gift</div>
    <div class="abs center display share__role" style="left:499px;top:190px">The<br>recipient</div>
    <div class="abs center share__note">What may not be obvious is that there should be some kind of connection.</div>
    <div class="mini-brand"><div class="mini-brand__deck">Lets get<br>back to<br>basics</div><div class="mini-brand__mark">Cortland<br>Circle</div></div>
  </section>

  <!-- Slide 5: throw or offer -->
  <section class="slide" style="left:734px;top:497px">
    <div class="abs center throw__title">How you communicare?</div>
    <div class="bar" style="top:119px;width:16px"></div>
    <div class="abs" style="left:35px;top:142px;width:100px">
      <div class="display throw__head">Do you<br>throw it?</div>
      <div class="throw__small">(Irrespective of the<br>person likes it or not.<br>just keep on throwing)</div>
      <div class="throw__face">☹</div>
    </div>
    <svg class="layer" viewBox="0 0 591 331">
      <defs>
        <linearGradient id="throwTone" x1="0" y1="0" x2="1" y2="1">
          <stop offset="0" stop-color="#f6efe6"/><stop offset="1" stop-color="#d9b48a"/>
        </linearGradient>
        <radialGradient id="offerTone" cx="50%" cy="50%" r="55%">
          <stop offset="0" stop-color="#e7a34a"/><stop offset=".55" stop-color="#f3ede4"/><stop offset="1" stop-color="#1d2440"/>
        </radialGradient>
      </defs>
      <circle cx="214" cy="181" r="64" fill="url(#throwTone)" stroke="var(--green)" role="img" aria-label="Illustration of cookies being thrown through the air"/>
      <circle cx="352" cy="181" r="64" fill="url(#offerTone)" stroke="var(--green)" role="img" aria-label="Photo of a plate of round cookies served with coffee"/>
    </svg>
    <div class="abs" style="left:434px;top:142px;width:130px">
      <div class="display throw__head">Or do you offer<br>it proudly</div>
      <div class="throw__small">(and wait for them to<br>take a bite and shower<br>you with praise?)</div>
      <div class="throw__face" style="margin-left:8px">☺</div>
    </div>
    <div class="mini-brand"><div class="mini-brand__deck">Lets get<br>back to<br>basics</div><div class="mini-brand__mark">Cortland<br>Circle</div></div>
  </section>

  <!-- Slide 3: the sharing flow -->
  <section class="slide" style="left:92px;top:844px">
    <div class="bar" style="top:105px;width:16px"></div>
    <svg class="layer" viewBox="0 0 591 331">
      <defs>
        <radialGradient id="giftTone" cx="50%" cy="45%" r="55%">
          <stop offset="0" stop-color="#b88150"/><stop offset=".55" stop-color="#e6d3bd"/><stop offset="1" stop-color="#ffffff"/>
        </radialGradient>
        <radialGradient id="recipientTone" cx="50%" cy="55%" r="60%">
          <stop offset="0" stop-color="#8a6a58"/><stop offset="1" stop-color="#2e2a28"/>
        </radialGradient>
      </defs>
      <circle cx="125" cy="192" r="72" fill="url(#giftTone)" stroke="var(--green)" role="img" aria-label="Photo of a hand holding out a chocolate chip cookie"/>
      <circle cx="299" cy="192" r="72" fill="url(#giftTone)" stroke="var(--green)" role="img" aria-label="Photo of two chocolate chip cookies"/>
      <circle cx="473" cy="192" r="72" fill="url(#recipientTone)" stroke="var(--green)" role="img" aria-label="Photo of a person happily taking a bite of a cookie"/>
      <g fill="var(--blue)" stroke="var(--green)" stroke-width="1">
        <circle cx="87" cy="114" r="28" fill="#fff"/><circle cx="87" cy="114" r="25" stroke="none"/>
        <circle cx="268" cy="114" r="28" fill="#fff"/><circle cx="268" cy="114" r="25" stroke="none"/>
        <circle cx="431" cy="114" r="28" fill="#fff"/><circle cx="431" cy="114" r="25" stroke="none"/>
      </g>
      <g fill="var(--green)">
        <path d="M206 187 h5 v-4 l7 8 -7 8 v-4 h-5z"/>
        <path d="M382 187 h5 v-4 l7 8 -7 8 v-4 h-5z"/>
      </g>
    </svg>
    <div class="abs center display flow__badge" style="left:87px;top:115px">Giver</div>
    <div class="abs center display flow__badge" style="left:268px;top:115px">The gift</div>
    <div class="abs center display flow__badge" style="left:431px;top:112px">The<br>recipient</div>
    <div class="abs center flow__caption" style="left:123px;top:286px">The one trying to communicate</div>
    <div class="abs center flow__caption" style="left:298px;top:286px">The message which is communicated</div>
    <div class="abs center flow__caption" style="left:473px;top:286px">The recipient who receives gift</div>
    <div class="mini-brand"><div class="mini-brand__deck">Lets get<br>back to<br>basics</div><div class="mini-brand__mark">Cortland<br>Circle</div></div>
  </section>

  <!-- Slide 6: you -->
  <section class="slide" style="left:735px;top:855px">
    <div class="bar bar--blue" style="top:100px"></div>
    <div class="abs center you__title">you</div>
    <svg class="layer" viewBox="0 0 591 331">
      <defs>
        <linearGradient id="personTone" x1="0" y1="0" x2="0" y2="1">
          <stop offset="0" stop-color="#7a3a34"/><stop offset=".35" stop-color="#3f6f9e"/><stop offset="1" stop-color="#324f72"/>
        </linearGradient>
      </defs>
      <g fill="#fff" stroke="var(--green)" stroke-width="1">
        <path d="M171 95 a68 60 0 1 1 -38 110 L124 222 L130 198 a68 60 0 0 1 41 -103z"/>
        <path d="M295 85 a55 44 0 1 1 30 82 L330 178 L318 168 a55 44 0 0 1 -23 -82z"/>
        <path d="M399 86 a55 52 0 1 1 -34 94 L358 194 L362 175 a55 52 0 0 1 34 -89z"/>
        <path d="M453 175 a56 48 0 1 1 -30 88 L418 275 L420 260 a56 48 0 0 1 10 -85z"/>
        <path d="M268 161 a40 34 0 1 1 -22 60 L236 230 L244 218 a40 34 0 0 1 24 -57z"/>
        <path d="M202 201 a42 36 0 1 1 22 66 L230 277 L218 268 a42 36 0 0 1 -20 -67z"/>
      </g>
      <rect x="292" y="190" width="80" height="141" fill="url(#personTone)" role="img" aria-label="Photo of a person seen from behind, thinking"/>
    </svg>
    <div class="abs center you__bubble" style="left:171px;top:157px">Your knowledge of<br>product, company,<br>customer</div>
    <div class="abs center you__bubble" style="left:296px;top:127px">Your role/<br>responsibilities</div>
    <div class="abs center you__bubble" style="left:399px;top:134px">Your goal<br>in the<br>communication</div>
    <div class="abs center you__bubble" style="left:268px;top:196px">Skill and<br>training</div>
    <div class="abs center you__bubble" style="left:202px;top:237px">Cognitive<br>biases</div>
    <div class="abs center you__bubble" style="left:460px;top:223px">Your<br>communication<br>style</div>
    <div class="mini-brand"><div class="mini-brand__deck">Lets get<br>back to<br>basics</div><div class="mini-brand__mark">Cortland<br>Circle</div></div>
  </section>

</div>
</div>
</body>
</html>
```